Creation of a page for funnel

Our company is specialized in insoles and well-being. Our insoles help reduce joint problems, stress or ink to promote weight loss. We need a clean and refined sales page, this one will be used on funnel click. The page should display the values of our product in first: "promote weight loss" in second: "Relieves muscle and joint pain" third: "Increases energy and stress stress". The page must be in the colors of our logo (green) if possible this color: light green: dark green 54c248. It is important to follow this model for the page with totally new and fresh desing: https: // lunavera-shop. uk / kto-rb Additionnal details for icons Section u: 1: "A unique design based on two types of knowledge" 2: "approved by acupressure expert" "Lose weight" 2: "Increases blood flow and oxygen in your body" 3: "Relieves muscle and joint pain" 4: "Increases energy and reduces stress" Section x: 1: "for men and women" 2: "one size "3:" Adjustable by cutting "Section y: 1:" powerful magnet in tourmaline "2:" for all type of shoes "3:" Flexible and light "4:" Breathable "Section z: 1:" free shipping "2 : "Customer service" 3: "money back guarantee" 4: "safe payment"
Target Market(s)
men and women 35
Number of Pages Required
1 page
Requirements
Must have
- the 5 sections mentioned in description
Nice to have
- some GIF like the funnel

```html
<!DOCTYPE html>
<html lang="en">
<head>
<meta charset="utf-8">
<title>StrideWell – Acupressure Insoles</title>
<link rel="stylesheet" href="https://fonts.googleapis.com/css2?family=Montserrat:wght@400;500;600;700&display=swap">
<style>
:root{
  --green:#3fd60f;
  --green-2:#4ad61a;
  --green-3:#36c80c;
  --green-dark:#2a9e0c;
  --green-text:#1f8a12;
  --mint:#eafde2;
  --mint-2:#f2fdee;
  --red-1:#7a0f12;
  --red-2:#b3242a;
  --ink:#2b2b2b;
  --grey:#6f6f6f;
  --footer:#3e3e3e;
  --white:#ffffff;
}
*{margin:0;padding:0;box-sizing:border-box}
html,body{width:1200px;height:3523px;overflow:hidden}
body{position:relative;background:var(--white);font-family:"Montserrat",Arial,sans-serif;color:var(--ink)}
.abs{position:absolute}
.btn{position:absolute;display:flex;flex-direction:column;align-items:center;justify-content:center;background:linear-gradient(90deg,var(--green-3),var(--green));color:var(--white);border-radius:30px;font-weight:700;font-size:12px;line-height:1.3;box-shadow:0 8px 18px rgba(63,214,15,.3);white-space:nowrap}
.btn small{font-size:10px;font-weight:600}
.brand{position:absolute;display:flex;align-items:center;gap:8px}
.brand-dot{width:22px;height:22px;border-radius:50%;background:var(--green)}
.brand-name{font-size:30px;font-weight:600;color:var(--green-dark);line-height:1;white-space:nowrap}
.brand-tag{position:absolute;font-size:11px;color:var(--grey);white-space:nowrap}
/* hero */
.hero-photo{left:0;top:0;width:1200px;height:700px;background:linear-gradient(110deg,#f6f3ef 0%,#efe4d9 35%,#f5ece2 60%,#faf7f3 100%)}
.hero-photo::after{content:"";position:absolute;inset:0;background:linear-gradient(90deg,rgba(255,255,255,.85),rgba(255,255,255,.35))}
.nav a{position:absolute;top:44px;font-size:12px;color:var(--ink);text-decoration:none;white-space:nowrap}
.hero-title{left:200px;top:174px;font-size:33px;font-weight:500;line-height:1.2;color:var(--ink)}
.hero-text{left:200px;top:302px;width:230px;font-size:11px;line-height:1.5;color:var(--grey)}
.insoles-hero{left:540px;top:100px;width:540px;height:560px;border-radius:200px 200px 120px 120px;background:radial-gradient(ellipse at 50% 50%,#ffffff,#e8eaec 70%,#d7dadd);transform:rotate(-6deg);z-index:3}
/* green benefits */
.benefits{left:0;top:530px;width:1200px;height:450px;clip-path:polygon(0 140px,1200px 0,1200px 450px,0 450px)}
.benefits .col{position:absolute;top:0;height:450px;width:400px}
.benefit{position:absolute;width:400px;text-align:center;color:var(--white);font-size:15px;line-height:1.45;z-index:4}
.benefit svg{display:block;margin:0 auto 14px}
/* red band */
.bloodflow{left:0;top:930px;width:1200px;height:770px;clip-path:polygon(0 30px,1200px 0,1200px 570px,0 760px);background:radial-gradient(ellipse at 55% 45%,#d4474c 0%,var(--red-2) 35%,var(--red-1) 100%)}
.bloodflow-lead{left:0;width:1200px;top:1093px;text-align:center;color:var(--white);font-size:16px;line-height:1.5;font-weight:500}
.flow-card{left:383px;top:1165px;width:436px;height:270px;background:var(--mint-2);clip-path:polygon(0 40px,100% 0,100% 100%,0 100%)}
.flow-title{left:383px;width:436px;top:1260px;text-align:center;font-size:26px;font-weight:600;color:var(--green-text)}
.flow-text{left:410px;width:382px;top:1300px;text-align:center;font-size:12px;line-height:1.6;color:var(--grey)}
.arrow-circle{width:32px;height:32px;border:1.5px solid rgba(255,255,255,.85);border-radius:50%;top:1466px;display:flex;align-items:center;justify-content:center}
/* specs */
.specs{left:0;top:1500px;width:1200px;height:630px;background:var(--mint);clip-path:polygon(0 190px,1200px 0,1200px 630px,0 545px)}
.spec{position:absolute;width:300px;text-align:center}
.spec svg{display:block;margin:0 auto 10px}
.spec h3{font-size:16px;font-weight:600;color:var(--ink);margin-bottom:8px}
.spec p{font-size:11px;line-height:1.5;color:var(--grey)}
/* features */
.insoles-pair{left:411px;top:2125px;width:387px;height:412px;border-radius:160px;background:radial-gradient(ellipse at 50% 50%,#ffffff,#eceef0 65%,#dcdfe2)}
.feature{position:absolute;width:200px}
.feature h3{font-size:16px;font-weight:500;line-height:1.35;color:var(--ink);margin-bottom:14px}
.feature p{font-size:11px;line-height:1.6;color:var(--grey)}
.feature.left{left:180px;text-align:right}
.feature.right{left:819px;text-align:left}
/* guarantees */
.perk{position:absolute;z-index:6;width:181px;background:var(--mint);text-align:center;padding-top:28px}
.perk svg{display:block;margin:0 auto 10px}
.perk h4{font-size:12px;font-weight:600;color:var(--ink);margin-bottom:10px;white-space:nowrap}
.perk p{font-size:11px;line-height:1.55;color:var(--grey);padding:0 18px}
/* footer */
.footer-green{left:0;top:2880px;width:1200px;height:300px;background:linear-gradient(90deg,var(--green) 0%,var(--green-2) 60%,var(--green-3) 100%);clip-path:polygon(0 0,1200px 40px,1200px 300px,0 300px);z-index:1}
.footer-dark{left:0;top:2885px;width:1200px;height:638px;background:var(--footer);clip-path:polygon(0 205px,1200px 0,1200px 638px,0 638px);z-index:2}
.footer-base{left:0;top:3380px;width:1200px;height:143px;background:var(--green-3);clip-path:polygon(0 143px,1200px 20px,1200px 143px);z-index:3}
.footer-col{position:absolute;z-index:4;color:#d8d8d8;font-size:11px;line-height:1.9;white-space:nowrap}
.footer-col h5{font-size:13px;font-weight:600;color:var(--white);margin-bottom:8px}
.footer-call{font-size:16px;color:var(--white);font-weight:500}
.footer-call span{color:var(--green)}
.pay{display:inline-block;width:24px;height:16px;border:1px solid #9a9a9a;border-radius:3px;margin-right:6px}
</style>
</head>
<body>

<div class="abs hero-photo" role="img" aria-label="Faded photo of a runner's legs and shoe on a track"></div>

<div class="brand" style="left:200px;top:26px;z-index:5"><span class="brand-dot"></span><span class="brand-name">StrideWell</span></div>
<div class="brand-tag" style="left:230px;top:58px;z-index:5">L'essayer c'est l'adopter !</div>

<nav class="nav" style="position:absolute;left:0;top:0;z-index:5">
  <a style="left:669px">How It Works</a>
  <a style="left:770px">Pricing</a>
  <a style="left:838px">FAQ</a>
</nav>
<div class="btn" style="left:916px;top:33px;width:110px;height:37px;z-index:5">Shop Now</div>

<h1 class="abs hero-title" style="z-index:5">Reduce joint<br>Pain, Stress and<br>weight loss</h1>
<p class="abs hero-text" style="z-index:5">Lorem ipsum dolor sit, consectetur adipiscing elit, sed do eiusmod tempor incididunt ut dolore magna aliqua.</p>
<div class="btn" style="left:200px;top:413px;width:159px;height:52px;z-index:5">Up To 68% Off<small>Shop Now!</small></div>
<svg class="abs" style="left:202px;top:530px;z-index:5" width="14" height="20" viewBox="0 0 14 20"><path d="M7 1v17M2 13l5 5 5-5" fill="none" stroke="var(--green)" stroke-width="1.5"/></svg>

<div class="abs insoles-hero" role="img" aria-label="Pair of white acupressure insoles with magnet points"></div>

<section class="abs benefits">
  <div class="col" style="left:0;background:var(--green)"></div>
  <div class="col" style="left:400px;background:var(--green-2)"></div>
  <div class="col" style="left:800px;background:var(--green-3)"></div>
</section>
<div class="benefit" style="left:0;top:790px">
  <svg width="56" height="50" viewBox="0 0 56 50"><path d="M28 48S3 32 3 16A12 12 0 0 1 28 10a12 12 0 0 1 25 6c0 16-25 32-25 32z" fill="#fff"/><path d="M38 30h12M44 24v12" stroke="var(--green)" stroke-width="4"/></svg>
  A totally natural solution with-<br>out any health risk
</div>
<div class="benefit" style="left:400px;top:728px">
  <svg width="50" height="54" viewBox="0 0 50 54"><circle cx="25" cy="22" r="20" fill="#fff"/><path d="M15 38l-6 14 9-4 5 6 2-12M35 38l6 14-9-4-5 6-2-12" fill="#fff"/><path d="M16 22l6 6 12-12" fill="none" stroke="var(--green-2)" stroke-width="4"/></svg>
  Approved by<br>acupressure expert
</div>
<div class="benefit" style="left:800px;top:666px">
  <svg width="48" height="48" viewBox="0 0 48 48"><circle cx="24" cy="24" r="22" fill="#fff"/><ellipse cx="18" cy="28" rx="5" ry="9" fill="var(--green-3)"/><ellipse cx="30" cy="20" rx="5" ry="9" fill="var(--green-3)"/></svg>
  A unique design based on two<br>types of knowledge
</div>

<section class="abs bloodflow" role="img" aria-label="Close-up of red blood cells flowing through a vessel"></section>
<p class="abs bloodflow-lead">Walk only 15min per day with<br>our product, you can ...</p>
<div class="abs flow-card"></div>
<h2 class="abs flow-title">Increases blood flow</h2>
<p class="abs flow-text">and oxygen throughout your body Lorem ipsum dolor sit amet, consectetur adipiscing elit, sed do eiusmod tempor</p>
<div class="btn" style="left:547px;top:1380px;width:106px;height:32px;font-size:11px">Shop Now!</div>
<div class="abs arrow-circle" style="left:563px"><svg width="10" height="10" viewBox="0 0 10 10"><path d="M7 1L3 5l4 4" fill="none" stroke="#fff" stroke-width="1.5"/></svg></div>
<div class="abs arrow-circle" style="left:603px"><svg width="10" height="10" viewBox="0 0 10 10"><path d="M3 1l4 4-4 4" fill="none" stroke="#fff" stroke-width="1.5"/></svg></div>

<section class="abs specs"></section>
<div class="spec" style="left:57px;top:1808px">
  <svg width="74" height="50" viewBox="0 0 74 50"><circle cx="22" cy="14" r="11" fill="var(--green-dark)"/><path d="M2 50c0-16 9-24 20-24s20 8 20 24z" fill="var(--green-dark)"/><circle cx="52" cy="14" r="11" fill="var(--green-3)"/><path d="M32 50c0-16 9-24 20-24s20 8 20 24z" fill="var(--green-3)"/></svg>
  <h3>For Men &amp; Women</h3>
  <p>Lorem Ipsum has been industry's standard<br>dummy text ever</p>
</div>
<div class="spec" style="left:451px;top:1752px">
  <svg width="60" height="54" viewBox="0 0 60 54"><ellipse cx="16" cy="32" rx="7" ry="13" fill="var(--green-dark)"/><ellipse cx="30" cy="22" rx="7" ry="13" fill="var(--green-3)"/><rect x="44" y="4" width="10" height="46" rx="2" fill="none" stroke="var(--green-dark)" stroke-width="3"/><path d="M44 14h5M44 24h5M44 34h5" stroke="var(--green-dark)" stroke-width="2"/></svg>
  <h3>One Size</h3>
  <p>Lorem Ipsum has been industry's standard<br>dummy text ever</p>
</div>
<div class="spec" style="left:848px;top:1700px">
  <svg width="52" height="52" viewBox="0 0 52 52"><circle cx="13" cy="40" r="8" fill="none" stroke="var(--green-dark)" stroke-width="4"/><circle cx="39" cy="40" r="8" fill="none" stroke="var(--green-dark)" stroke-width="4"/><path d="M18 34L40 4M34 34L12 4" stroke="var(--green-3)" stroke-width="5" stroke-linecap="round"/></svg>
  <h3>Adjustable By Cutting</h3>
  <p>Lorem Ipsum has been industry's standard<br>dummy text ever</p>
</div>

<div class="abs insoles-pair" role="img" aria-label="Top view of a pair of white magnetic insoles"></div>
<div class="feature left" style="top:2195px"><h3>Powerful magnet<br>in tourmaline</h3><p>Lorem ipsum dolor sit amet, consectetur adipiscing elit, sed do eiusmod tempor incididunt ut labore et dolore magna.</p></div>
<div class="feature left" style="top:2358px"><h3>Ultra Breathable<br>Insoles</h3><p>Lorem ipsum dolor sit amet, consectetur adipiscing elit, sed do eiusmod tempor incididunt ut labore et dolore magna.</p></div>
<div class="feature right" style="top:2195px"><h3>For all type<br>of shoes</h3><p>Lorem ipsum dolor sit amet, consectetur adipiscing elit, sed do eiusmod tempor incididunt ut labore et dolore magna.</p></div>
<div class="feature right" style="top:2358px"><h3>Flexible and<br>light</h3><p>Lorem ipsum dolor sit amet, consectetur adipiscing elit, sed do eiusmod tempor incididunt ut labore et dolore magna.</p></div>
<div class="btn" style="left:520px;top:2602px;width:160px;height:52px">Up To 68% Off<small>Shop Now!</small></div>

<div class="perk" style="left:200px;top:2755px;height:200px">
  <svg width="30" height="22" viewBox="0 0 30 22"><path d="M1 3h17v13H1zM18 8h6l5 5v3h-11z" fill="none" stroke="var(--green-dark)" stroke-width="2"/><circle cx="7" cy="18" r="3" fill="#fff" stroke="var(--green-dark)" stroke-width="2"/><circle cx="23" cy="18" r="3" fill="#fff" stroke="var(--green-dark)" stroke-width="2"/></svg>
  <h4>Free Shipping</h4><p>Lorem ipsum dolor sit amet, consectetur adipiscing elit, sed eiusmod.</p>
</div>
<div class="perk" style="left:406px;top:2730px;height:240px;background:var(--mint-2)">
  <svg width="26" height="30" viewBox="0 0 26 30"><circle cx="13" cy="9" r="7" fill="none" stroke="var(--green-dark)" stroke-width="2"/><path d="M2 29c0-8 5-12 11-12s11 4 11 12" fill="none" stroke="var(--green-dark)" stroke-width="2"/></svg>
  <h4>Customer Service</h4><p>Lorem ipsum dolor sit amet, consectetur adipiscing elit, sed eiusmod.</p>
</div>
<div class="perk" style="left:613px;top:2755px;height:200px">
  <svg width="28" height="28" viewBox="0 0 28 28"><path d="M22 8a10 10 0 1 1-6-4" fill="none" stroke="var(--green-dark)" stroke-width="2"/><path d="M14 1l4 3-3 4" fill="none" stroke="var(--green-dark)" stroke-width="2"/></svg>
  <h4>100% Money Back</h4><p>Lorem ipsum dolor sit amet, consectetur adipiscing elit, sed eiusmod.</p>
</div>
<div class="perk" style="left:819px;top:2755px;height:200px">
  <svg width="24" height="28" viewBox="0 0 24 28"><rect x="2" y="12" width="20" height="15" rx="2" fill="none" stroke="var(--green-dark)" stroke-width="2"/><path d="M6 12V8a6 6 0 0 1 12 0v4" fill="none" stroke="var(--green-dark)" stroke-width="2"/><circle cx="12" cy="19" r="2" fill="var(--green-dark)"/></svg>
  <h4>Safe Payment</h4><p>Lorem ipsum dolor sit amet, consectetur adipiscing elit, sed eiusmod.</p>
</div>

<div class="abs footer-green"></div>
<div class="abs footer-dark"></div>
<div class="abs footer-base"></div>
<svg class="abs" style="left:1092px;top:3000px;z-index:4" width="14" height="20" viewBox="0 0 14 20"><path d="M7 19V2M2 7l5-5 5 5" fill="none" stroke="var(--green)" stroke-width="1.5"/></svg>

<div class="brand" style="left:200px;top:3160px;z-index:4"><span class="brand-dot"></span><span class="brand-name" style="color:var(--green)">StrideWell</span></div>
<div class="brand-tag" style="left:230px;top:3192px;z-index:4;color:#d8d8d8">L'essayer c'est l'adopter !</div>
<div class="footer-col" style="left:200px;top:3214px">Copyright © 2019 StrideWell.<br>All Rights Reserved.</div>

<div class="footer-col" style="left:512px;top:3154px">
  <h5>Support</h5>
  <div class="footer-call">Call. <span>+33 1 84 60 22 15</span></div>
  e. hello@stridewell-shop.com<br>How It Works<br>Pricing<br>FAQ
</div>
<div class="footer-col" style="left:819px;top:3154px">
  <h5>Info</h5>
  Shipping &amp; Return<br>Terms of Sales<br>Terms of use<br>Privacy
</div>
<div class="footer-col" style="left:200px;top:3370px;font-size:10px">
  Safe &amp; Secure Payment<br>
  <span class="pay"></span><span class="pay"></span><span class="pay"></span><span class="pay"></span><span class="pay"></span>
</div>

</body>
</html>
```